Business Card

I want our business cards to have a little more pizzazz. I like the content, and we are in healthcare (so nothing to wild or artsy), but something that allows our cards to stand out.

Business

```html
<!DOCTYPE html>
<html lang="en">
<head>
<meta charset="utf-8">
<title>Norvale Medical – Business Card</title>
<link href="https://fonts.googleapis.com/css2?family=Questrial&display=swap" rel="stylesheet">
<style>
  :root {
    --navy: #1b5790;
    --sky: #6f9cc6;
    --sky-light: #a9c6e2;
    --cream: #f1efe2;
    --ink: #2e2e2e;
    --rule: #c9c6b6;
    --backdrop: #e6e8eb;
  }
  * { margin: 0; padding: 0; box-sizing: border-box; }
  html, body { width: 1200px; height: 786px; overflow: hidden; }
  body {
    background: var(--backdrop);
    font-family: "Questrial", "Century Gothic", sans-serif;
    display: flex; align-items: center; justify-content: center; gap: 48px;
  }
  .card {
    position: relative; width: 540px; height: 309px;
    border-radius: 16px; overflow: hidden;
    box-shadow: 0 6px 18px rgba(0,0,0,.18);
  }
  .brand { display: flex; align-items: center; gap: 12px; }
  .brand-mark { width: 22px; height: 22px; flex: none; background: var(--navy); }
  .brand-name { display: flex; flex-direction: column; line-height: 1.02; }

  /* Front */
  .card-front { background: var(--cream); }
  .front-wave { position: absolute; left: 0; bottom: 0; width: 100%; height: 100%; }
  .front-brand { position: absolute; left: 34px; top: 66px; }
  .front-brand .brand-name { color: var(--navy); font-size: 30px; }
  .divider { position: absolute; left: 256px; top: 48px; width: 1px; height: 124px; background: var(--rule); }
  .contact { position: absolute; left: 276px; top: 46px; width: 248px; color: var(--ink); font-size: 13.5px; line-height: 1.42; }
  .person-name { color: var(--navy); font-size: 17px; letter-spacing: .06em; font-weight: 400; }
  .person-title { font-size: 13px; margin-bottom: 6px; }
  .contact-list { list-style: none; }
  .contact-list li { display: flex; align-items: center; gap: 8px; white-space: nowrap; }
  .contact-icon { width: 13px; height: 13px; flex: none; }
  .address { margin-top: 6px; }

  /* Back */
  .card-back { background: var(--navy); color: #fff; }
  .back-brand { position: absolute; left: 0; right: 0; top: 46px; justify-content: center; }
  .back-brand .brand-mark { background: #fff; width: 26px; height: 26px; }
  .back-brand .brand-name { color: #fff; font-size: 34px; }
  .service-band {
    position: absolute; left: 0; right: 0; top: 150px; height: 64px;
    background: var(--sky); display: flex; flex-direction: column; justify-content: center; align-items: center;
    font-size: 15px; line-height: 1.45; letter-spacing: .02em;
  }
  .hotline { position: absolute; left: 0; right: 0; top: 232px; text-align: center; font-size: 13px; line-height: 1.45; color: #e3ecf5; }
</style>
</head>
<body>
  <section class="card card-front">
    <svg class="front-wave" viewBox="0 0 540 309" preserveAspectRatio="none" aria-hidden="true">
      <path d="M0 222 C120 236 210 262 290 309 L0 309 Z" fill="var(--sky-light)"/>
      <path d="M0 232 C110 244 200 272 262 309 L0 309 Z" fill="var(--sky)"/>
      <path d="M0 250 C90 258 170 284 210 309 L0 309 Z" fill="var(--navy)"/>
    </svg>
    <div class="brand front-brand">
      <span class="brand-mark"></span>
      <span class="brand-name"><span>Norvale</span><span>Medical</span></span>
    </div>
    <div class="divider"></div>
    <div class="contact">
      <h1 class="person-name">DANIEL MORENO</h1>
      <p class="person-title">Territory Manager</p>
      <ul class="contact-list">
        <li><svg class="contact-icon" viewBox="0 0 13 13"><rect width="13" height="13" rx="2" fill="var(--navy)"/><rect x="4" y="2.5" width="5" height="8" rx="1" fill="none" stroke="#fff" stroke-width="1.1"/></svg>(555) 014-7116</li>
        <li><svg class="contact-icon" viewBox="0 0 13 13"><rect width="13" height="13" rx="2" fill="var(--navy)"/><path d="M3.5 3 L5.5 3 L6 5 L5 6 C5.6 7.2 6 7.6 7 8 L8 7 L10 7.5 L10 9.5 C6 9.8 3.2 7 3.5 3 Z" fill="#fff"/></svg>(555) 010-1100</li>
        <li><svg class="contact-icon" viewBox="0 0 13 13"><rect width="13" height="13" rx="2" fill="var(--navy)"/><rect x="3" y="5" width="7" height="5" fill="#fff"/><rect x="4.5" y="2.5" width="4" height="3" fill="none" stroke="#fff" stroke-width="1"/></svg>(555) 012-0008</li>
        <li><svg class="contact-icon" viewBox="0 0 13 13"><rect width="13" height="13" rx="2" fill="var(--navy)"/><rect x="2.5" y="3.5" width="8" height="6" fill="none" stroke="#fff" stroke-width="1"/><path d="M2.5 3.5 L6.5 7 L10.5 3.5" fill="none" stroke="#fff" stroke-width="1"/></svg>daniel.moreno@norvalemed.com</li>
      </ul>
      <p class="address">48 Harbor Street<br>Millbrook, NJ 07000</p>
    </div>
  </section>

  <section class="card card-back">
    <div class="brand back-brand">
      <span class="brand-mark"></span>
      <span class="brand-name"><span>Norvale</span><span>Medical</span></span>
    </div>
    <div class="service-band">
      <p>Servicing Laboratories · Hospital &amp; Medical centers</p>
      <p>Research Facilities · Surgical Centers</p>
    </div>
    <p class="hotline">If you can't reach me, please call our<br>Customer Service Hotline at 555.010.1111</p>
  </section>
</body>
</html>
```